Stationery and Business Card Design

We need stationary design for our new company pelvanta. Pelvanta is a company that provides city apartment rentals for tourists in Athens We need business cards, letterheads for A4 and A5 and envelopes for A4 A5. The design needs to be modern, friendly and corporate.

Target Market(s)

City Tourists

Industry/Entity Type

Tourism

```html
<!DOCTYPE html>
<html lang="en">
<head>
<meta charset="utf-8">
<title>Pelvanta Apartments – Stationery</title>
<link rel="stylesheet" href="https://fonts.googleapis.com/css2?family=Raleway:wght@400;500;700&family=Arimo:wght@400&family=Roboto:wght@400;500&family=Dancing+Script:wght@700&display=swap">
<style>
  :root {
    --brand: #950052;
    --ink: #222222;
    --muted: #555555;
    --paper: #ffffff;
    --stage: #e3e3e5;
    --base-dark: #444446;
    --base-grey: #666668;
  }
  * { box-sizing: border-box; margin: 0; padding: 0; }
  html, body { width: 1189px; height: 1200px; overflow: hidden; background: var(--stage); }
  .canvas { position: relative; width: 1189px; height: 1200px; }
  .sheet { position: absolute; overflow: hidden; }
  .band { position: absolute; background: var(--brand); }
  .base { position: absolute; left: 0; right: 0; bottom: 0; }
  .mark-square { position: absolute; background: var(--brand); }
  .wordmark {
    position: absolute; left: 0; right: 0; text-align: center;
    font-family: "Raleway", sans-serif; font-weight: 400; color: var(--brand); line-height: 1;
  }
  .tagline {
    position: absolute; left: 0; right: 0; display: flex; justify-content: center; align-items: center;
    font-family: "Raleway", sans-serif; color: var(--brand); letter-spacing: .32em; line-height: 1;
  }
  .tagline::before, .tagline::after { content: ""; height: 1px; background: currentColor; opacity: .7; }

  /* A4 letterhead */
  .letter-a4 { left: 50px; top: 110px; width: 507px; height: 657px; background: var(--paper); }
  .letter-a4 .wordmark { top: 70px; font-size: 36px; }
  .letter-a4 .tagline { top: 105px; font-size: 8.5px; gap: 8px; }
  .letter-a4 .tagline::before, .letter-a4 .tagline::after { width: 28px; background: var(--muted); }
  .recipient { position: absolute; left: 41px; top: 154px; font-family: "Roboto", sans-serif; color: var(--ink); }
  .recipient .name { font-size: 10px; font-weight: 500; letter-spacing: .02em; margin-bottom: 5px; }
  .recipient p { font-size: 8.4px; line-height: 10.5px; }
  .letter-body { position: absolute; left: 41px; top: 242px; width: 432px; font-family: "Arimo", sans-serif; font-size: 8.9px; line-height: 14.9px; color: var(--ink); }
  .letter-body p + p { margin-top: 14.9px; }
  .signoff { position: absolute; left: 41px; top: 479px; font-family: "Arimo", sans-serif; font-size: 8.9px; color: var(--ink); }
  .signature { position: absolute; left: 40px; top: 497px; font-family: "Dancing Script", cursive; font-size: 32px; color: var(--ink); }
  .signer { position: absolute; left: 41px; top: 542px; font-family: "Roboto", sans-serif; font-size: 9.5px; line-height: 12px; color: var(--ink); }
  .signer .name { font-weight: 500; }
  .footer-rule { position: absolute; left: 43px; top: 595px; width: 422px; height: 3px; background: var(--brand); }
  .footer-info { position: absolute; left: 43px; top: 605px; width: 430px; display: flex; align-items: center; font-family: "Raleway", sans-serif; font-size: 8px; line-height: 10px; color: var(--muted); }
  .footer-info .col { display: flex; flex-direction: column; }
  .footer-info .divider { width: 1.5px; height: 18px; background: var(--brand); margin: 0 24px; }
  .icon-line { display: flex; align-items: center; gap: 5px; }
  .icon { display: inline-block; width: 8px; height: 8px; flex: none; }

  /* Folder */
  .folder { left: 629px; top: 111px; width: 506px; height: 653px; background: var(--brand); }
  .folder .mark-square { left: 228px; top: 279px; width: 50px; height: 50px; background: var(--paper); }
  .folder .wordmark { top: 331px; font-size: 36px; color: var(--paper); }
  .folder .tagline { top: 367px; font-size: 8.5px; gap: 8px; color: var(--paper); }
  .folder .tagline::before, .folder .tagline::after { width: 28px; }
  .folder .web { position: absolute; left: 0; right: 0; top: 619px; text-align: center; font-family: "Raleway", sans-serif; font-size: 9px; color: var(--paper); }

  /* A5 letterhead */
  .letter-a5 { left: 51px; top: 833px; width: 332px; height: 234px; background: var(--paper); }
  .letter-a5 .wordmark { left: 0; right: auto; width: 129px; top: 54px; font-size: 17px; }
  .letter-a5 .tagline { left: 0; right: auto; width: 129px; top: 73px; font-size: 4.5px; gap: 4px; }
  .letter-a5 .tagline::before, .letter-a5 .tagline::after { width: 14px; background: var(--muted); }
  .letter-a5 .address { position: absolute; left: 20px; top: 214px; font-family: "Raleway", sans-serif; font-size: 4.2px; color: var(--muted); }

  /* Envelope */
  .envelope { left: 472px; top: 832px; width: 333px; height: 234px; background: var(--brand); }
  .flap { position: absolute; left: 0; top: 0; width: 333px; height: 54px; }

  /* Business cards */
  .card { width: 215px; }
  .card-front { left: 921px; top: 805px; height: 122px; background: var(--brand); }
  .card-front .mark-square { left: 96px; top: 39px; width: 22px; height: 21px; background: var(--paper); }
  .card-front .wordmark { top: 64px; font-size: 15px; color: var(--paper); }
  .card-front .tagline { top: 80px; font-size: 4px; gap: 3px; color: var(--paper); }
  .card-front .tagline::before, .card-front .tagline::after { width: 12px; }
  .card-front .web { position: absolute; left: 0; right: 0; top: 107px; text-align: center; font-family: "Raleway", sans-serif; font-size: 5.5px; color: var(--paper); }

  .card-back { left: 921px; top: 953px; height: 123px; background: var(--paper); }
  .card-back .wordmark { top: 43px; font-size: 15px; }
  .card-back .tagline { top: 60px; font-size: 4px; gap: 3px; }
  .card-back .tagline::before, .card-back .tagline::after { width: 12px; background: var(--muted); }
  .card-details { position: absolute; left: 0; right: 0; top: 84px; display: flex; font-family: "Raleway", sans-serif; color: var(--muted); }
  .card-details .who { width: 104px; text-align: right; font-size: 5.4px; line-height: 7px; }
  .card-details .who .name { font-size: 8px; font-weight: 700; color: var(--brand); line-height: 10px; }
  .card-details .divider { width: 1px; height: 24px; background: var(--brand); margin: 2px 6px 0; }
  .card-details .reach { font-size: 5.4px; line-height: 7px; }
  .card-details .icon { width: 5px; height: 5px; }
  .card-details .icon-line { gap: 3px; }
</style>
</head>
<body>
<main class="canvas">

  <!-- A4 letterhead -->
  <section class="sheet letter-a4" aria-label="A4 letterhead">
    <div class="band" style="left:0;top:15px;width:171px;height:50px"></div>
    <div class="band" style="left:336px;top:15px;right:0;height:50px"></div>
    <div class="mark-square" style="left:228px;top:15px;width:50px;height:50px"></div>
    <div class="wordmark">Pelvanta</div>
    <div class="tagline">APARTMENTS</div>

    <div class="recipient">
      <div class="name">MARA ELLIS</div>
      <p>Street Name,City Name.</p>
      <p>Zip Coad 0000</p>
    </div>

    <div class="letter-body">
      <p>Lorem Ipsum is simply dummy text of the printing and typesetting industry. Lorem Ipsum has been the industry’s standard dummy text ever since the 1500s, when an unknown printer took a galley of type and scrambled it to make a type specimen book. It has survived not only five centuries, but also the leap into electronic typesetting, remaining essentially unchanged. It was popularised in the 1960s with the release of Letraset sheets containing Lorem Ipsum passages, and more recently with desktop publishing software like Aldus PageMaker including versions of Lorem Ipsum.</p>
      <p>It is a long established fact that a reader will be distracted by the readable content of a page when looking at its layout. The point of using Lorem Ipsum is that it has a more-or-less normal distribution of letters, as opposed to using ‘Content here, content here’, making it look like readable English. Many desktop publishing packages and web page editors now use Lorem Ipsum as their default model text, and a search for ‘lorem ipsum’ will uncover many web sites still in their infancy. Various versions have evolved over the years, sometimes by accident, sometimes on purpose (injected humour and the like).</p>
    </div>

    <div class="signoff">Regards,</div>
    <div class="signature">Theo Varga</div>
    <div class="signer">
      <div class="name">Theo Varga</div>
      <div>General Maneger</div>
    </div>

    <div class="footer-rule"></div>
    <div class="footer-info">
      <div class="col">
        <span class="icon-line"><svg class="icon" viewBox="0 0 8 8"><rect width="8" height="8" rx="1" fill="#950052"/><path d="M2.3 1.8l1 1-.5.7c.4.8.9 1.3 1.7 1.7l.7-.5 1 1-.7.8C3.9 6.3 1.7 4.1 1.5 2.5z" fill="#fff"/></svg>000-000-0000</span>
        <span class="icon-line"><svg class="icon" viewBox="0 0 8 8"><rect width="8" height="8" rx="1" fill="#950052"/><rect x="1.6" y="3" width="4.8" height="3" fill="#fff"/><rect x="2.4" y="1.5" width="3.2" height="1.2" fill="#fff"/></svg>000-000-0000</span>
      </div>
      <div class="divider"></div>
      <div class="col">
        <span class="icon-line"><svg class="icon" viewBox="0 0 8 8"><rect width="8" height="8" rx="1" fill="#950052"/><circle cx="4" cy="4" r="2.4" fill="none" stroke="#fff" stroke-width=".8"/><path d="M1.6 4h4.8" stroke="#fff" stroke-width=".6"/></svg>www.yourcompanyweb.com</span>
        <span class="icon-line"><svg class="icon" viewBox="0 0 8 8"><rect width="8" height="8" rx="1" fill="#950052"/><rect x="1.5" y="2.3" width="5" height="3.4" fill="none" stroke="#fff" stroke-width=".7"/><path d="M1.5 2.3L4 4.3l2.5-2" fill="none" stroke="#fff" stroke-width=".7"/></svg>yourcompany@yourgmail.com</span>
      </div>
      <div class="divider"></div>
      <div class="col" style="margin-left:4px">
        <span>P.O Box 0000 Your Address</span>
        <span>2nd Street,New Zeland</span>
      </div>
    </div>
    <div class="base" style="height:15px;background:var(--base-dark)"></div>
  </section>

  <!-- Presentation folder -->
  <section class="sheet folder" aria-label="Presentation folder">
    <div class="mark-square"></div>
    <div class="wordmark">Pelvanta</div>
    <div class="tagline">APARTMENTS</div>
    <div class="web">www.yourcompany.com</div>
    <div class="base" style="height:14px;background:var(--base-grey)"></div>
  </section>

  <!-- A5 letterhead -->
  <section class="sheet letter-a5" aria-label="A5 letterhead">
    <div class="band" style="left:0;top:23px;width:20px;height:26px"></div>
    <div class="band" style="left:110px;top:23px;right:0;height:26px"></div>
    <div class="mark-square" style="left:51px;top:23px;width:27px;height:27px"></div>
    <div class="wordmark">Pelvanta</div>
    <div class="tagline">APARTMENTS</div>
    <div class="address">0000 Youe Address,2nd Ste. Rivermont, State 1234</div>
    <div class="base" style="height:9px;background:var(--base-dark)"></div>
  </section>

  <!-- Envelope -->
  <section class="sheet envelope" aria-label="Envelope">
    <svg class="flap" viewBox="0 0 333 54" aria-hidden="true">
      <path d="M0 0H333L326 44Q325 51 318 51H15Q8 51 7 44Z" fill="#ffffff"/>
    </svg>
    <div class="mark-square" style="left:148px;top:9px;width:35px;height:35px"></div>
  </section>

  <!-- Business card, front -->
  <section class="sheet card card-front" aria-label="Business card front">
    <div class="mark-square"></div>
    <div class="wordmark">Pelvanta</div>
    <div class="tagline">APARTMENTS</div>
    <div class="web">www.yourcompany.com</div>
    <div class="base" style="height:7px;background:var(--base-grey)"></div>
  </section>

  <!-- Business card, back -->
  <section class="sheet card card-back" aria-label="Business card back">
    <div class="band" style="left:0;top:16px;width:69px;height:24px"></div>
    <div class="band" style="left:149px;top:16px;right:0;height:24px"></div>
    <div class="mark-square" style="left:96px;top:16px;width:24px;height:24px"></div>
    <div class="wordmark">Pelvanta</div>
    <div class="tagline">APARTMENTS</div>
    <div class="card-details">
      <div class="who">
        <div class="name">Employee Name</div>
        <div>0000 Youe Address,2nd Ste.</div>
        <div>Rivermont, State 1234</div>
      </div>
      <div class="divider"></div>
      <div class="reach">
        <div class="icon-line"><svg class="icon" viewBox="0 0 8 8"><rect width="8" height="8" fill="#950052"/></svg>000 000 0000</div>
        <div class="icon-line"><svg class="icon" viewBox="0 0 8 8"><rect width="8" height="8" fill="#950052"/></svg>yourcompany@gmail.com</div>
        <div class="icon-line"><svg class="icon" viewBox="0 0 8 8"><rect width="8" height="8" fill="#950052"/></svg>www.yourcompany.com</div>
      </div>
    </div>
    <div class="base" style="height:7px;background:var(--base-dark)"></div>
  </section>

</main>
</body>
</html>
```